Lorraine Whitcombe Resume 2025

🎨 Design Aesthetic
Overall Look: Sophisticated, clean, minimalist — less “corporate template,” more “editorial/luxury brand.” Think Interiors Quarterly meets Pemberly Global Estates.
Colors:
Base: Warm white or ivory background (instead of stark white, which can feel clinical).
Accents: Soft taupe, blush beige, muted rose-gold, warm gray. These lean feminine, elegant, and upscale without being distracting.
Avoid heavy blacks — use charcoal gray for text.
🔤 Typography
You’ll want fonts that are timeless, system-available (no downloading), and upscale. Pairing one serif with one sans-serif is a proven high-end combo.
Primary Serif (for Name + Section Headers):
Georgia (classic, built-in)
Times New Roman (if you want ultra-traditional, though a bit expected)
Palatino Linotype (a softer, elegant serif)
Secondary Sans-serif (for body text):
Helvetica Neue (clean, luxury feel)
Calibri (simple, highly readable, professional)
Arial Narrow (refined but modern)
✨ Recommended pairing: Name/Headings in Georgia Bold + Body in Helvetica Neue Light → refined, professional, easy to use in all your collateral.
📐 Layout & Structure
Header (Top Third):
Your name large, centered or left-aligned.
Subline with phone, email, location in smaller font, spaced out with dividers (e.g., |).
Neutral line or subtle accent bar under the header (warm gray or muted blush).
Section Layout:
Plenty of white space (breathe between sections, upscale feel).
Clear section headers (all caps serif font, spaced letters for luxury look).
Use subtle horizontal rules in a soft accent color instead of thick lines.
Accents:
Very subtle shading in soft beige or blush for section backgrounds (not blocks, just highlights).
Icons kept minimal — avoid anything too “clip-arty.”
🖼 Visual Mood Reference
Imagine:
A high-end boutique hotel brand sheet
Valdine packaging tones (ivory, taupe, gold accent) but dialed down to be subtle
Editorial spacing like in Lustre or Nido Home
🗂 Sections to Highlight (for your pivot)
Profile / Objective – Short 2–3 lines at the top making clear you are pivoting into luxury real estate, with transferable leadership skills.
Experience – KTR Studio (as Owner, not Managing Partner) with emphasis on entrepreneurship, strategy, client growth.
Board Membership – Whitcombe Foundation role (philanthropy adds prestige).
Certifications – Shows discipline and learning.
Education – Clean, simple.
“I want a resume design that feels refined and luxury-oriented, clean and sophisticated, with soft neutral feminine tones (ivory, blush beige, taupe, warm gray). Font pairing should be elegant but standard (e.g., Georgia for headings + Helvetica Neue for body) so I can reuse across collateral without downloading special fonts. Layout should have lots of white space, understated lines/dividers, and feel like something you’d expect from a luxury real estate or fashion brand.”

```html
<!DOCTYPE html>
<html lang="en">
<head>
<meta charset="utf-8">
<title>Lorraine Whitcombe — Resume 2025</title>
<link href="https://fonts.googleapis.com/css2?family=Gelasio:wght@400;600;700&family=Roboto+Condensed:wght@300;400;600&display=swap" rel="stylesheet">
<style>
  :root{
    --canvas:#84919b;
    --blush:#f1d8cc;
    --ivory:#f7f0e6;
    --stripe:#fbf7f1;
    --taupe:#bfa296;
    --charcoal:#2c3a49;
    --body:#58626c;
    --dot:#c2a69b;
    --rule:#efcfc3;
  }
  *{margin:0;padding:0;box-sizing:border-box}
  html,body{width:1200px;height:1200px;overflow:hidden;background:var(--canvas)}
  .page{position:absolute;left:150px;top:18px;width:899px;height:1164px;background:var(--ivory);overflow:hidden;
    font-family:"Roboto Condensed",Arial,sans-serif;font-weight:300;color:var(--body)}
  .band{position:absolute;left:0;width:100%;background:var(--blush)}
  .band--top{top:0;height:363px;border-bottom:5px solid var(--stripe)}
  .band--bottom{top:920px;height:244px;border-top:5px solid var(--stripe)}
  .serif{font-family:"Gelasio",Georgia,serif}
  .abs{position:absolute}

  .name{left:75px;font-family:"Gelasio",Georgia,serif;font-weight:700;line-height:1}
  .name--first{top:62px;font-size:54px;color:var(--taupe);letter-spacing:1px}
  .name--last{top:105px;font-size:77px;color:var(--ivory);letter-spacing:-0.5px}
  .contact{left:75px;font-family:Arial,Helvetica,sans-serif;font-weight:400;font-size:15px;letter-spacing:2.6px;color:var(--charcoal)}
  .contact--phone{top:244px}
  .contact--email{top:283px}

  .portrait{left:285px;top:45px;width:370px;height:520px;border-radius:185px 185px 40px 40px;
    background:radial-gradient(ellipse at 50% 28%, #e9c9b4 0 22%, #e2c79a 30%, rgba(238,230,220,.9) 52%, rgba(245,242,238,.6) 72%, rgba(247,240,230,0) 85%);
    -webkit-mask-image:linear-gradient(to bottom,#000 70%,transparent 100%);mask-image:linear-gradient(to bottom,#000 70%,transparent 100%)}

  .bio{left:585px;top:66px;width:250px;font-size:12.3px;line-height:15.8px;color:var(--body)}
  .bio p+p{margin-top:15.8px}
  .bio b{font-weight:600;color:var(--charcoal)}

  .section-title{font-family:"Gelasio",Georgia,serif;font-weight:700;font-size:43px;line-height:1}
  .section-title--experience{left:77px;top:430px;color:var(--charcoal);letter-spacing:9px}
  .section-title--certs{left:77px;top:954px;color:var(--taupe);letter-spacing:11px}

  .role-head{font-family:"Gelasio",Georgia,serif;font-weight:700;color:var(--charcoal);font-size:18.5px;line-height:1}
  .role-sub{font-family:"Gelasio",Georgia,serif;font-weight:700;color:var(--charcoal);font-size:13px}
  .date{font-size:14px;color:var(--body);line-height:1}
  .para{font-size:12.3px;line-height:15.8px}
  .bullets{list-style:none;font-size:10.8px;line-height:14px}
  .bullets li{position:relative;padding-left:16px;margin-bottom:14px}
  .bullets li::before{content:"";position:absolute;left:2px;top:5px;width:4px;height:4px;border-radius:50%;background:var(--dot)}

  .certs{left:77px;top:1012px;width:700px;font-size:10.8px;line-height:14px}
  .cert{position:absolute;width:200px}
  .cert b{display:block;font-weight:600;color:var(--charcoal)}
  .updated{left:751px;top:1023px;width:79px;height:72px;background:var(--ivory);padding:16px 0 0 11px;font-size:10.8px;line-height:14px}
  .edu-rule{left:623px;top:475px;width:204px;height:2px;background:var(--rule)}
</style>
</head>
<body>
<div class="page">
  <div class="band band--top"></div>
  <div class="band band--bottom"></div>

  <div class="abs portrait" role="img" aria-label="Portrait photograph of Lorraine Whitcombe in a white blazer"></div>

  <div class="abs name name--first">Lorraine</div>
  <div class="abs name name--last">Whitcombe</div>
  <div class="abs contact contact--phone">(555) 014-2768</div>
  <div class="abs contact contact--email">lorraine@ktrstudio.com</div>

  <div class="abs bio">
    <p>Lorraine Whitcombe is an industry-leading media strategist and entrepreneur with <b>15+ years of experience across multiple industries.</b></p>
    <p>As <b>Owner of the award-winning EDWOSB-certified agency KTR Studio Inc.</b>, she drives performance across multiple departments and acts as an internal strategic advisor. Her expertise spans government project management and corporate workflows, providing a rare combination of entrepreneurship, leadership, and marketing strategy.</p>
    <p>Lorraine is now pursuing a full-time career in <b>real estate</b>, bringing her skills in negotiation, business development, and client relations to the Miami luxury market.</p>
  </div>

  <div class="abs section-title section-title--experience">Experience</div>

  <div class="abs role-head" style="left:77px;top:500px">KTR Studio, Inc.</div>
  <div class="abs role-sub" style="left:257px;top:502px">Owner</div>
  <div class="abs date" style="left:319px;top:501px">2007 – Present</div>
  <p class="abs para" style="left:77px;top:536px;width:330px">As a business owner in the media and marketing space, Lorraine brings innovative insight and marketing ideas, becoming an industry expert for every client. Her creativity, flexibility, transparency, and results-driven approach lend to long-term partnerships across all business verticals. By working closely with clients, her teams create powerful media and marketing campaigns that engage and inspire.</p>

  <div class="abs role-head" style="left:79px;top:650px;font-size:15px">Key Accomplishments</div>
  <ul class="abs bullets" style="left:78px;top:683px;width:320px">
    <li>Scaled KTR Studio Inc.’s client base both commercially and federally during the COVID-19 pandemic.</li>
    <li>Conceptualized and organized large-scale campaigns while leading KTR to immense success despite market disruptions.</li>
    <li>Directed Northstar Service Corps campaigns across<br>13+ states in the past 12 months.</li>
    <li>For the Northstar Service Corps (Minnesota), overhauled marketing efforts to be data-driven and high-performing, delivering 3M+ impressions, 700+ conversions (2.58% conversion rate), and a 533% decreased CPA (from $901 to $48 at launch).</li>
  </ul>

  <div class="abs role-head" style="left:631px;top:397px">Education</div>
  <div class="abs date" style="left:750px;top:400px;width:77px;text-align:right">1993 – 1998</div>
  <div class="abs role-sub" style="left:631px;top:422px;line-height:16px">Lakeshore University<br>Bachelor of Arts, Sociology</div>
  <div class="abs edu-rule"></div>

  <div class="abs role-head" style="left:466px;top:542px">Board Membership</div>
  <div class="abs date" style="left:700px;top:545px;width:107px;text-align:right">2018 – Present</div>
  <div class="abs role-sub" style="left:466px;top:571px;width:360px;line-height:16px">Active Board Member,<br>The Sylvia Whitcombe &amp; William W. Whitcombe Memorial Foundation (The Whitcombe Foundation)</div>
  <p class="abs para" style="left:466px;top:634px;width:345px">As a business owner in the media and marketing space, Lorraine brings innovative insight and marketing ideas, becoming an industry expert for every client. Her creativity, flexibility, transparency, and results-driven approach lend to long-term partnerships across all business verticals. By working closely with clients, her teams create powerful media and marketing campaigns that engage and inspire.</p>
  <ul class="abs bullets" style="left:467px;top:759px;width:340px">
    <li>Support governance, fundraising, and philanthropic initiatives dedicated to advancing music education and instrument preservation.</li>
    <li>Collaborate with fellow board members to ensure compliance, organizational growth, and mission alignment.</li>
    <li>Represent family legacy and oversee strategic initiatives benefiting communities nationwide.</li>
  </ul>

  <div class="abs section-title section-title--certs">Certifications</div>

  <div class="abs certs">
    <div class="cert" style="left:0;top:0">Leadership for Sales and Marketing Professionals<b>Corvane Global Systems, Inc., 2018</b></div>
    <div class="cert" style="left:232px;top:0">Reachwell Email Marketing Certification<b>2019</b></div>
    <div class="cert" style="left:425px;top:0">Executive Playbook: Managing the 3 C’s, Change, Conflict, and Communications<b>Corvane, 2019</b></div>
    <div class="cert" style="left:0;top:57px">Scaling Excellence Across the Organization<b>Corvane Global Systems, Inc., 2019</b></div>
    <div class="cert" style="left:232px;top:57px">Reachwell Email Marketing Certification<b>2019</b></div>
    <div class="cert" style="left:425px;top:57px">21st Century Leadership<b>Corvane Global Systems, Inc., 2020</b></div>
  </div>

  <div class="abs updated">UPDATED<br>September 8,<br>2025</div>
</div>
</body>
</html>
```